Brisvane Partners Web Design

Dear all
I need a web design for a financial services site. We are a broker who deals with many different financial institutions and require a clean, simple and instantly impressive site based on the colour scheme that Mockwell created for us. A landing page (www.brisvn.mx) gives an idea of the logo and clour scheme but we are looking at either a one page site with rollover text boxes or a 3 or 4 page site depending on the preference of the designer and the best user experience. The site“s purpose is to give confidence that the company exists rather than impart pages of information although we would like this to be a site that can expand over time as the company grows. For now the requirement is for a clear set of possibly changing images at the centre of a white screen that relate to finance in general nad the benefits of wealth creation as well as sectios either along the top or bottom - Our Company, Our Approach, Our services, Our clients, Contact (user to fill in contact box to be sent to info@brisvn.mx. The text for each of these boxes I assume can be added by the coding team here, it the overall look and feel that I am looking for from Mockwell - deadline can be extended if necessary but I was hoping to wrap this all up in October

Target Market(s)

Succesful individuals looking to maximise returns on their investment via world class financial institutions and supported throughout by qualified independent financial advisors

Industry/Entity Type

Finance

Requirements
Must have
• Logo and color scheme of the logo design Mockwell sent - I have all these sourcefiles, pantone and fonts

```html
<!DOCTYPE html>
<html lang="en">
<head>
<meta charset="utf-8">
<title>Brisvane Partners</title>
<link rel="stylesheet" href="https://fonts.googleapis.com/css2?family=Questrial&family=PT+Sans:wght@400;700&family=Open+Sans:wght@400;600&display=swap">
<style>
  :root {
    --white: #ffffff;
    --navy: #1d3461;
    --navy-panel: rgba(29, 58, 108, 0.9);
    --navy-dark: #14213b;
    --orange: #f0a03a;
    --ink: #2a2a2a;
    --muted-blue: #a9b8d2;
    --grey-band: #8a8c90;
    --icon-grey: #b7b9bc;
    --photo-a: #c9ced6;
    --photo-b: #6f7f99;
    --photo-c: #e2e4e7;
  }
  * { margin: 0; padding: 0; box-sizing: border-box; }
  html, body { width: 1200px; height: 740px; overflow: hidden; background: var(--white); }
  body { position: relative; font-family: "Open Sans", sans-serif; color: var(--ink); }

  .site-header { position: absolute; left: 0; top: 0; width: 1200px; height: 106px; background: var(--white); }
  .brand { position: absolute; left: 216px; top: 40px; display: flex; align-items: center; gap: 8px;
    font-family: "Questrial", sans-serif; font-size: 17px; letter-spacing: 3px; color: var(--navy); }
  .brand-mark { width: 14px; height: 14px; border-radius: 50%; background: var(--navy); }
  .main-nav { position: absolute; top: 70px; left: 0; width: 1200px; height: 36px; }
  .main-nav a { position: absolute; top: 0; font-family: "Questrial", sans-serif; font-size: 16px;
    letter-spacing: 0.5px; color: var(--ink); text-decoration: none; text-transform: uppercase; }
  .main-nav a.is-active::after { content: ""; position: absolute; left: -1px; right: -1px; top: 30px; height: 4px; background: var(--orange); }

  .hero { position: absolute; left: 0; top: 106px; width: 1200px; height: 531px; }
  .hero-photo { position: absolute; inset: 0;
    background: radial-gradient(ellipse at 75% 20%, var(--photo-b) 0%, rgba(111,127,153,0) 45%),
                linear-gradient(160deg, var(--photo-c) 0%, var(--photo-a) 55%, #b3b8bf 100%); }
  .feature-panel { position: absolute; left: 0; top: 44px; width: 540px; height: 383px; background: var(--navy-panel); }
  .feature-title { position: absolute; left: 194px; top: 40px; font-family: "PT Sans", sans-serif; font-weight: 700;
    font-size: 26px; line-height: 28px; color: var(--white); text-transform: uppercase; }
  .feature-text { position: absolute; left: 194px; top: 136px; width: 330px; font-size: 12.5px; line-height: 20px; color: var(--muted-blue); }
  .feature-link { position: absolute; left: 409px; top: 328px; font-size: 12.5px; font-weight: 600; color: var(--white);
    text-decoration: none; display: flex; align-items: center; gap: 12px; }
  .feature-link svg { width: 7px; height: 11px; }
  .panel-strip { position: absolute; left: 0; top: 427px; width: 540px; height: 10px; background: #9da2aa; }

  .section-menu { position: absolute; left: 688px; top: 173px; width: 204px; list-style: none; }
  .section-menu li { position: relative; height: 36px; line-height: 36px; padding-left: 27px; font-size: 11.5px;
    color: var(--white); background: linear-gradient(90deg, var(--navy-dark), var(--navy));
    border-bottom: 1px solid rgba(170, 185, 210, 0.45); }
  .section-menu li:last-child { border-bottom: 0; }
  .section-menu li.is-current::before { content: ""; position: absolute; left: 0; top: 0; border-top: 18px solid var(--orange); border-right: 18px solid transparent; }

  .slide-next { position: absolute; left: 948px; top: 206px; width: 38px; height: 76px; }
  .scroll-down { position: absolute; left: 566px; top: 466px; width: 70px; height: 40px; }

  .footer-band { position: absolute; left: 0; top: 637px; width: 1200px; height: 9px; background: var(--grey-band); }
  .site-footer { position: absolute; left: 0; top: 646px; width: 1200px; height: 94px; }
  .copyright { position: absolute; left: 198px; top: 24px; font-size: 11px; line-height: 17px; color: var(--ink); }
  .social { position: absolute; left: 851px; top: 37px; display: flex; gap: 12px; list-style: none; }
  .social li { width: 25px; height: 25px; background: var(--icon-grey); }
</style>
</head>
<body>
  <header class="site-header">
    <div class="brand"><span class="brand-mark"></span>BRISVANE</div>
    <nav class="main-nav">
      <a href="#" style="left:491px">Home</a>
      <a href="#" class="is-active" style="left:568px">About us</a>
      <a href="#" style="left:673px">Works</a>
      <a href="#" style="left:767px">Services</a>
      <a href="#" style="left:853px">Blog</a>
      <a href="#" style="left:909px">Contact</a>
    </nav>
  </header>

  <section class="hero">
    <div class="hero-photo" role="img" aria-label="Blurred photo of a businessman working at a laptop"></div>

    <article class="feature-panel">
      <h1 class="feature-title">Financial solution<br>for your business</h1>
      <p class="feature-text">Lorem ipsum dolor sit amet, consectetuer adipiscing elit, sed diam nonummy nibh euismod tincidunt ut laoreet dolore magna aliquam erat volutpat. Ut wisi enim ad minim veniam, quis nostrud exerci tation ullamcorper sus-cipit lobortis nisl.</p>
      <a class="feature-link" href="#">View detail
        <svg viewBox="0 0 7 11"><path d="M0 0 L7 5.5 L0 11 Z" fill="#f0a03a"/></svg>
      </a>
    </article>
    <div class="panel-strip"></div>

    <ul class="section-menu">
      <li class="is-current">Our Company</li>
      <li>Our Approach</li>
      <li>Our Services</li>
      <li>Our Clients</li>
    </ul>

    <svg class="slide-next" viewBox="0 0 38 76"><path d="M4 2 L34 38 L4 74" fill="none" stroke="#3a4150" stroke-width="4"/></svg>
    <svg class="scroll-down" viewBox="0 0 70 40"><path d="M2 2 L35 36 L68 2" fill="none" stroke="#3a4150" stroke-width="4"/></svg>
  </section>

  <div class="footer-band"></div>
  <footer class="site-footer">
    <p class="copyright">Copyright ©&nbsp; 2013. Brisvane Partners<br>All rights reserved.</p>
    <ul class="social">
      <li aria-label="Social link"></li>
      <li aria-label="Social link"></li>
      <li aria-label="Social link"></li>
      <li aria-label="Feed link"></li>
    </ul>
  </footer>
</body>
</html>
```